GreenGlider Powerpoint Template Project

Develop a custom .ppt template that effectively communicates the GreenGlider value proposition and can be tailored for our different audiences: retail partnerships, strategic partnerships, institutional funding and end customers. Our studies have shown a massive improvement in putting effectiveness when using the GreenGlider solution for just 3-5 minutes per day. We would like this dramatic result to be front and center of our value proposition. Putting makes up a huge percentage of a golfer's score (over 40%), but it's widely known that the average golfer spends very little time practicing putting. Reasons for this are reported as: "it's boring"; "tedious"; "it's easy, so I don't need to practice as much"; "I'd rather spend my limited time with the full swing". Using the GreenGlider, golfers can vastly improve their putting effectiveness with significantly less time and effort than other practice methods. Our company mantra, "precision practice" is the "how" in our solution, but ROPI - Return on Parctice Investment - is our real value proposition.
Target Market(s)
Golfers age 18 to 75 with low-medium to high disposable income
Industry/Entity Type
Sports and Leisure

```html
<!DOCTYPE html>
<html lang="en">
<head>
<meta charset="utf-8">
<title>GreenGlider Presentation Template</title>
<link href="https://fonts.googleapis.com/css2?family=Montserrat:wght@400;500;600;700&display=swap" rel="stylesheet">
<style>
:root{
  --red:#e31e24;
  --black:#1c1c1e;
  --stage:#c9c9c9;
  --light:#ececec;
  --mid:#8a8a8a;
  --white:#ffffff;
  --grass:#5f8a3a;
  --sky:#a9c3d6;
}
*{margin:0;padding:0;box-sizing:border-box}
html,body{width:1200px;height:1104px;overflow:hidden}
body{background:var(--stage);font-family:'Montserrat',sans-serif;color:var(--black);position:relative}
.slide{position:absolute;width:246px;height:138px;background:var(--white);overflow:hidden;box-shadow:0 1px 3px rgba(0,0,0,.25)}
.slide.dark{background:var(--black);color:var(--white)}
.abs{position:absolute}
.title{position:absolute;left:12px;top:7px;font-size:6.3px;font-weight:500;letter-spacing:.2px}
.title.red{color:var(--red);font-weight:700}
.title.bold{font-weight:700}
.tiny{font-size:2.5px;line-height:1.35}
.small{font-size:3.2px;line-height:1.3}
.caps{text-transform:uppercase}
.footer{position:absolute;left:0;bottom:0;width:100%;height:7px;background:var(--red)}
.footer-name{position:absolute;left:12px;top:2px;font-size:2.8px;color:var(--white)}
.brand{position:absolute;right:8px;top:0;height:7px;padding:0 2px;background:var(--white);display:flex;align-items:center;gap:1.5px;font-size:3.2px;font-weight:700;color:var(--black)}
.brand-dot{width:4px;height:4px;border-radius:50%;background:var(--red)}
.photo{position:absolute}
.photo-golf{background:linear-gradient(180deg,#9bb8cc 0%,#6f9150 45%,#3f6a2a 100%)}
.photo-green{background:radial-gradient(circle at 50% 70%,#79a83f 0%,#4c7a2a 60%,#2e4f1c 100%)}
.photo-round{border-radius:50%}
.red-bar{position:absolute;height:1px;background:var(--red)}
ul.list{list-style:none}
ul.list li::before{content:"- ";}
</style>
</head>
<body>

<!-- Cover -->
<section class="slide dark" style="left:497px;top:43px;width:245px">
  <div class="red-bar" style="left:12px;top:33px;width:14px"></div>
  <p class="abs caps" style="left:12px;top:40px;width:90px;font-size:5.6px;line-height:1.3">Lorem ipsum dolor sit amet, consectetuer adipiscing elit, sed di</p>
  <div class="abs" style="left:0;top:74px;width:80px;height:25px;background:var(--white);display:flex;align-items:center;justify-content:center;gap:3px">
    <span class="brand-dot" style="width:8px;height:8px"></span><span style="font-size:7px;font-weight:700">GreenGlider</span>
  </div>
  <div class="photo photo-golf photo-round" style="left:115px;top:17px;width:105px;height:105px" role="img" aria-label="Golfer mid-swing on a course"></div>
</section>

<!-- Agenda -->
<section class="slide" style="left:66px;top:204px">
  <h2 class="title bold">AGENDA</h2>
  <div class="abs photo-round" style="left:6px;top:14px;width:108px;height:108px;border:3px solid var(--black)"></div>
  <div class="photo photo-green photo-round" style="left:12px;top:20px;width:96px;height:96px" role="img" aria-label="Golf ball on green grass with trees behind"></div>
  <ol class="abs small caps" style="left:140px;top:30px;list-style:none;font-size:3px;line-height:1.95">
    <li>02 &nbsp;Vision</li><li>03 &nbsp;About</li><li>04 &nbsp;Our Team</li><li>05 &nbsp;Summary</li><li>06 &nbsp;Vision</li><li>07 &nbsp;About</li><li>08 &nbsp;Our Team</li><li>09 &nbsp;Summary</li><li>10 &nbsp;Vision</li><li>11 &nbsp;About</li><li>12 &nbsp;Our Team</li><li>13 &nbsp;Summary</li>
  </ol>
  <div class="red-bar" style="left:140px;top:103px;width:14px"></div>
  <p class="abs tiny caps" style="left:140px;top:105px;width:76px">Lorem ipsum dolor sit amet, consectetuer adipiscing elit, sed diam nonummy nibh euismod tincidunt ut laoreet dolore magna aliquam erat volutpat. Ut wisi enim ad minim veniam, quis n</p>
  <div class="footer"><span class="footer-name">Presentation Name 2022</span><span class="brand"><i class="brand-dot"></i>GreenGlider</span></div>
</section>

<!-- Our Team -->
<section class="slide dark" style="left:360px;top:204px">
  <svg class="abs" style="left:0;top:0" width="246" height="138"><polygon points="222,0 246,0 246,138 160,138" fill="#fff"/></svg>
  <h2 class="title">OUR TEAM</h2>
  <div class="abs" style="left:12px;top:18px;width:160px;display:grid;grid-template-columns:1fr 1fr;column-gap:10px;row-gap:12px">
    <div><div style="display:flex;align-items:center;gap:3px"><span style="width:11px;height:11px;border-radius:50%;background:#9a9a9a" role="img" aria-label="Portrait of team member"></span><span class="small caps">Sam Whitlock<br>Director</span></div><p class="tiny" style="margin-top:3px">Sam leads product work and shapes every drill around short daily sessions. Sam tests each routine with club golfers before launch and keeps the program simple, fast and fun.</p></div>
    <div><div style="display:flex;align-items:center;gap:3px"><span style="width:11px;height:11px;border-radius:50%;background:#9a9a9a" role="img" aria-label="Portrait of team member"></span><span class="small caps">Sam Whitlock<br>Director</span></div><p class="tiny" style="margin-top:3px">Sam leads product work and shapes every drill around short daily sessions. Sam tests each routine with club golfers before launch and keeps the program simple, fast and fun.</p></div>
    <div><div style="display:flex;align-items:center;gap:3px"><span style="width:11px;height:11px;border-radius:50%;background:#9a9a9a" role="img" aria-label="Portrait of team member"></span><span class="small caps">Sam Whitlock<br>Director</span></div><p class="tiny" style="margin-top:3px">Sam leads product work and shapes every drill around short daily sessions.</p></div>
    <div><div style="display:flex;align-items:center;gap:3px"><span style="width:11px;height:11px;border-radius:50%;background:#9a9a9a" role="img" aria-label="Portrait of team member"></span><span class="small caps">Sam Whitlock<br>Director</span></div><p class="tiny" style="margin-top:3px">Sam leads product work and shapes every drill around short daily sessions.</p></div>
  </div>
  <div class="footer"><span class="footer-name">Presentation Name 2022</span><span class="brand"><i class="brand-dot"></i>GreenGlider</span></div>
</section>

<!-- Pricing -->
<section class="slide" style="left:642px;top:204px">
  <svg class="abs" style="left:0;top:0" width="246" height="138"><polygon points="0,0 246,0 246,30 0,83" fill="#e31e24"/></svg>
  <h2 class="title" style="color:#fff">PRICING</h2>
  <p class="abs tiny" style="left:12px;top:20px;width:108px;color:#fff">Lorem ipsum dolor sit amet, consectetuer adipiscing elit, sed diam nonummy nibh euismod tincidunt ut laoreet dolore magna aliquam erat volutpat. Ut wisi enim ad minim veniam, quis nostrud exerci tation ullamcorper suscipit lobortis nisl ut aliquip ex ea commodo consequat.</p>
  <div class="abs small" style="left:14px;top:89px"><p class="caps" style="font-size:2.9px">Entry Level</p><p style="margin-top:6px;font-size:4px">$3690</p><ul class="list tiny" style="margin-top:2px"><li>Small meetings</li><li>Small meetings</li><li>Small meetings</li><li>Small meetings</li></ul></div>
  <div class="abs" style="left:66px;top:73px;width:.5px;height:46px;background:#bbb"></div>
  <div class="abs small" style="left:70px;top:75px"><p class="caps" style="font-size:2.9px">Mid-Level</p><p style="margin-top:6px;font-size:4px">$4290</p><ul class="list tiny" style="margin-top:2px"><li>Small meetings</li><li>Small meetings</li><li>Small meetings</li><li>Small meetings</li></ul></div>
  <div class="abs" style="left:122px;top:61px;width:.5px;height:46px;background:#bbb"></div>
  <div class="abs small" style="left:127px;top:61px"><p class="caps" style="font-size:2.9px">Advanced</p><p style="margin-top:6px;font-size:4px">$4890</p><ul class="list tiny" style="margin-top:2px"><li>Small meetings</li><li>Small meetings</li><li>Small meetings</li><li>Small meetings</li></ul></div>
  <div class="abs" style="left:178px;top:47px;width:.5px;height:46px;background:#bbb"></div>
  <div class="abs small" style="left:182px;top:46px"><p class="caps" style="font-size:2.9px">Premium</p><p style="margin-top:6px;font-size:4px">$5490</p><ul class="list tiny" style="margin-top:2px"><li>Small meetings</li><li>Small meetings</li><li>Small meetings</li><li>Small meetings</li></ul></div>
  <div class="footer"><span class="footer-name">Presentation Name 2022</span><span class="brand"><i class="brand-dot"></i>GreenGlider</span></div>
</section>

<!-- Graphic 01 -->
<section class="slide" style="left:914px;top:204px">
  <div class="abs" style="left:0;top:0;width:70px;height:138px;background:var(--black)"></div>
  <h2 class="title" style="color:#fff">GRAPHIC 01</h2>
  <p class="abs caps" style="left:12px;top:20px;width:54px;color:#fff;font-size:3px;line-height:1.25">Lorem ipsum dolor sit amet, consectetuer adipiscing elit, sed diam nonummy nibh euismod tincidunt ut laoreet</p>
  <p class="abs tiny" style="left:12px;top:50px;width:54px;color:#fff">Practice putting for three to five minutes a day and track each stroke gained. Our players saw steady gains in touch, line and speed within weeks. Short focused drills beat long sessions on the range, and golfers stay keen because every minute counts toward a lower score.</p>
  <svg class="abs" style="left:90px;top:50px" width="130" height="76">
    <rect x="10" y="8" width="9" height="65" fill="#1c1c1e"/>
    <rect x="38" y="12" width="9" height="61" fill="#1c1c1e"/>
    <rect x="68" y="38" width="9" height="35" fill="#1c1c1e"/>
    <rect x="96" y="46" width="9" height="27" fill="#1c1c1e"/>
    <line x1="0" y1="73.5" x2="125" y2="73.5" stroke="#ddd" stroke-width=".5"/>
  </svg>
  <div class="footer"><span class="footer-name">Presentation Name 2022</span><span class="brand"><i class="brand-dot"></i>GreenGlider</span></div>
</section>

<!-- Graphic 02 -->
<section class="slide" style="left:66px;top:367px">
  <div class="photo photo-golf" style="left:0;top:0;width:246px;height:82px" role="img" aria-label="Golfer finishing a drive on a hilly course"></div>
  <h2 class="title bold" style="color:#fff">GRAPHIC 02</h2>
  <div class="abs" style="left:0;top:75px;width:246px;display:grid;grid-template-columns:repeat(5,1fr);padding:0 10px;text-align:center">
    <div><span style="display:inline-flex;width:15px;height:15px;border-radius:50%;background:var(--red);color:#fff;font-size:2.5px;align-items:center;justify-content:center">2014</span><p class="tiny" style="margin-top:4px;color:#666">Project One</p><p class="tiny" style="margin-top:7px">Marketers</p><p class="tiny" style="margin-top:4px">Track each putt to learn what works</p></div>
    <div><span style="display:inline-flex;width:15px;height:15px;border-radius:50%;background:var(--black);color:#fff;font-size:2.5px;align-items:center;justify-content:center">2015</span><p class="tiny" style="margin-top:4px;color:#666">Project Two</p><p class="tiny" style="margin-top:7px">Marketers</p><p class="tiny" style="margin-top:4px">Track each putt to learn what works</p></div>
    <div><span style="display:inline-flex;width:15px;height:15px;border-radius:50%;background:var(--red);color:#fff;font-size:2.5px;align-items:center;justify-content:center">2016</span><p class="tiny" style="margin-top:4px;color:#666">Project Three</p><p class="tiny" style="margin-top:7px">Marketers</p><p class="tiny" style="margin-top:4px">Track each putt to learn what works</p></div>
    <div><span style="display:inline-flex;width:15px;height:15px;border-radius:50%;background:var(--black);color:#fff;font-size:2.5px;align-items:center;justify-content:center">2017</span><p class="tiny" style="margin-top:4px;color:#666">Project Four</p><p class="tiny" style="margin-top:7px">Marketers</p><p class="tiny" style="margin-top:4px">Track each putt to learn what works</p></div>
    <div><span style="display:inline-flex;width:15px;height:15px;border-radius:50%;background:var(--red);color:#fff;font-size:2.5px;align-items:center;justify-content:center">2018</span><p class="tiny" style="margin-top:4px;color:#666">Project Five</p><p class="tiny" style="margin-top:7px">Marketers</p><p class="tiny" style="margin-top:4px">Track each putt to learn what works</p></div>
  </div>
  <div class="footer"><span class="footer-name">Presentation Name 2022</span><span class="brand"><i class="brand-dot"></i>GreenGlider</span></div>
</section>

<!-- Checkmark -->
<section class="slide" style="left:360px;top:367px">
  <h2 class="title red">CHECKMARK</h2>
  <p class="abs tiny" style="left:12px;top:17px;width:110px">Lorem ipsum dolor sit amet, consectetuer adipiscing elit, sed diam nonummy nibh euismod tincidunt ut laoreet dolore magna aliquam erat volutpat. Ut wisi enim ad minim veniam, quis nostrud exerci tation ullamcorper suscipit lobortis nisl ut aliquip ex ea commodo consequat. Duis autem vel eum iriure dolor in hendrerit in vulputate velit esse molestie consequat.</p>
  <svg class="abs" style="left:0;top:0" width="246" height="138"><polygon points="0,67 246,67 246,82 182,122 0,122" fill="#1c1c1e"/></svg>
  <div class="abs tiny" style="left:12px;top:72px;width:190px;display:grid;grid-template-columns:repeat(6,1fr);gap:5px;color:#fff">
    <div>&#10004;<br>To protect customers' digital experiences and secure their privacy.</div>
    <div>&#10004;<br>To protect customers' digital experiences and secure their privacy.</div>
    <div>&#10004;<br>To protect customers' digital experiences and secure their privacy.</div>
    <div>&#10004;<br>To protect customers' digital experiences and secure their privacy.</div>
    <div>&#10004;<br>To protect customers' digital experiences and secure their privacy.</div>
    <div>&#10004;<br>To protect customers' digital experiences and secure their privacy.</div>
  </div>
  <div class="footer"><span class="footer-name">Presentation Name 2022</span><span class="brand"><i class="brand-dot"></i>GreenGlider</span></div>
</section>

<!-- Graphic 03 -->
<section class="slide" style="left:642px;top:367px">
  <h2 class="title red">GRAPHIC 03</h2>
  <p class="abs tiny" style="left:40px;top:26px;color:#777">Sales</p>
  <p class="abs tiny" style="left:134px;top:26px;color:#777">Sales</p>
  <svg class="abs" style="left:12px;top:33px" width="60" height="50" viewBox="0 0 50 50"><g transform="rotate(-90 25 25)"><circle cx="25" cy="25" r="12" fill="none" stroke="#a6a6a6" stroke-width="24" stroke-dasharray="45 75.4"/><circle cx="25" cy="25" r="12" fill="none" stroke="#7c7c7c" stroke-width="24" stroke-dasharray="0 45 18 75.4"/><circle cx="25" cy="25" r="12" fill="none" stroke="#4a4a4a" stroke-width="24" stroke-dasharray="0 63 7.5 75.4"/><circle cx="25" cy="25" r="12" fill="none" stroke="#222" stroke-width="24" stroke-dasharray="0 70.5 5 75.4"/></g></svg>
  <svg class="abs" style="left:106px;top:33px" width="60" height="50" viewBox="0 0 50 50"><g transform="rotate(-90 25 25)"><circle cx="25" cy="25" r="12" fill="none" stroke="#a6a6a6" stroke-width="24" stroke-dasharray="45 75.4"/><circle cx="25" cy="25" r="12" fill="none" stroke="#7c7c7c" stroke-width="24" stroke-dasharray="0 45 18 75.4"/><circle cx="25" cy="25" r="12" fill="none" stroke="#4a4a4a" stroke-width="24" stroke-dasharray="0 63 7.5 75.4"/><circle cx="25" cy="25" r="12" fill="none" stroke="#222" stroke-width="24" stroke-dasharray="0 70.5 5 75.4"/></g></svg>
  <p class="abs tiny" style="left:12px;top:86px;color:#888;font-size:2px">&#9679; 1st Qtr &#9679; 2nd Qtr &#9679; 3rd Qtr &#9679; 4th Qtr</p>
  <p class="abs tiny" style="left:106px;top:86px;color:#888;font-size:2px">&#9679; 1st Qtr &#9679; 2nd Qtr &#9679; 3rd Qtr &#9679; 4th Qtr</p>
  <p class="abs tiny" style="left:12px;top:95px;width:74px">Lorem ipsum dolor sit amet, consectetuer adipiscing elit, sed diam nonummy nibh euismod tincidunt ut laoreet dolore magna aliquam erat volutpat. Ut wisi enim ad minim veniam, quis nostrud exerci tation ullamcorper suscipit lobortis nisl ut aliquip ex ea commodo consequat.</p>
  <p class="abs tiny" style="left:106px;top:95px;width:74px">Lorem ipsum dolor sit amet, consectetuer adipiscing elit, sed diam nonummy nibh euismod tincidunt ut laoreet dolore magna aliquam erat volutpat. Ut wisi enim ad minim veniam, quis nostrud exerci tation ullamcorper suscipit lobortis nisl ut aliquip ex ea commodo consequat.</p>
  <div class="footer"><span class="footer-name">Presentation Name 2022</span><span class="brand"><i class="brand-dot"></i>GreenGlider</span></div>
</section>

<!-- About Us -->
<section class="slide" style="left:914px;top:367px">
  <h2 class="title red" style="top:8px">ABOUT US</h2>
  <div class="abs" style="left:0;top:26px;width:246px;height:34px;background:var(--black)"></div>
  <p class="abs caps" style="left:12px;top:32px;width:170px;color:#fff;font-size:3px;line-height:1.25">Lorem ipsum dolor sit amet, consectetuer adipiscing elit, sed diam nonummy nibh euismod tincidunt ut laoreet dolore magna aliquam erat volutpat. Ut wisi enim ad minim veniam, quis nostrud exerci tation ullamcorper suscipit</p>
  <p class="abs tiny" style="left:12px;top:71px;width:72px">Lorem ipsum dolor sit amet, consectetuer adipiscing elit, sed diam nonummy nibh euismod tincidunt ut laoreet dolore magna aliquam erat volutpat. Ut wisi enim ad minim veniam, quis nostrud exerci tation ullamcorper suscipit lobortis nisl ut aliquip ex ea commodo consequat. Duis autem vel eum iriure dolor in hendrerit in vulputate velit esse molestie consequat.</p>
  <p class="abs tiny" style="left:97px;top:71px;width:72px">Lorem ipsum dolor sit amet, consectetuer adipiscing elit, sed diam nonummy nibh euismod tincidunt ut laoreet dolore magna aliquam erat volutpat. Ut wisi enim ad minim veniam, quis nostrud exerci tation ullamcorper suscipit lobortis nisl ut aliquip ex ea commodo consequat. Duis autem vel eum iriure dolor in hendrerit in vulputate velit esse molestie consequat.</p>
  <div class="footer"><span class="footer-name">Presentation Name 2022</span><span class="brand"><i class="brand-dot"></i>GreenGlider</span></div>
</section>

<!-- About Us 2 -->
<section class="slide dark" style="left:66px;top:548px">
  <div class="photo photo-green" style="left:100px;top:0;width:146px;height:138px" role="img" aria-label="Hand placing a golf ball on the green"></div>
  <svg class="abs" style="left:0;top:0" width="246" height="138"><polygon points="0,0 145,0 115,138 0,138" fill="#1c1c1e"/></svg>
  <h2 class="title red">ABOUT US 2</h2>
  <p class="abs caps" style="left:12px;top:38px;width:54px;color:var(--red);font-size:3px;line-height:1.25">Lorem ipsum dolor sit amet, consectetuer adipiscing elit, sed diam nonummy nibh euismod tincidunt ut laoreet</p>
  <p class="abs tiny" style="left:75px;top:37px;width:42px;color:#fff">Lorem ipsum dolor sit amet, consectetuer adipiscing elit, sed diam nonummy nibh euismod tincidunt ut laoreet dolore magna aliquam erat volutpat. Ut wisi enim ad minim veniam, quis nostrud exerci tation ullamcorper suscipit lobortis nisl ut aliquip ex ea commodo consequat. Duis autem vel eum iriure dolor in hendrerit in vulputate velit esse molestie consequat, vel illum dolore eu feugiat</p>
  <div class="footer"><span class="footer-name">Presentation Name 2022</span><span class="brand"><i class="brand-dot"></i>GreenGlider</span></div>
</section>

<!-- Table -->
<section class="slide" style="left:360px;top:548px">
  <h2 class="title red">TABLE</h2>
  <div class="abs" style="left:0;top:20px;width:246px;height:41px;background:var(--red)"></div>
  <p class="abs tiny" style="left:12px;top:23px;width:222px;color:#fff">Lorem ipsum dolor sit amet, consectetuer adipiscing elit, sed diam nonummy nibh euismod tincidunt ut laoreet dolore magna aliquam erat volutpat. Ut wisi enim ad minim veniam, quis nostrud exerci tation ullamcorper suscipit lobortis nisl ut aliquip ex ea commodo consequat. Duis autem vel eum iriure dolor in hendrerit in vulputate velit esse molestie consequat, vel illum dolore eu feugiat nulla facilisis. Lorem ipsum dolor sit amet, cons ectetuer adipiscing elit, sed dia<br><br>m nonummy nibh euismod tincidunt ut laoreet dolore magna aliquam erat volutpat. Ut wisi enim ad minim veniam, quis nostrud exerci tation ullamcorper suscipit lobortis nisl ut aliquip ex ea commodo consequat.</p>
  <table class="abs tiny" style="left:12px;top:65px;width:126px;border-collapse:separate;border-spacing:0 1.2px;font-size:2.2px">
    <thead><tr style="background:var(--black);color:#fff"><th style="text-align:left;padding:.4px 3px;font-weight:500">BASE</th><th style="text-align:left;padding:.4px 3px;font-weight:500">SCORE</th></tr></thead>
    <tbody>
      <tr style="background:var(--light)"><td style="padding:.4px 3px">AVERAGE MONTHLY QUOTES</td><td style="padding:.4px 3px">432</td></tr>
      <tr style="background:var(--light)"><td style="padding:.4px 3px">AVERAGE MONTHLY QUOTES</td><td style="padding:.4px 3px">946</td></tr>
      <tr style="background:var(--light)"><td style="padding:.4px 3px">AVERAGE MONTHLY QUOTES</td><td style="padding:.4px 3px">350</td></tr>
      <tr style="background:var(--light)"><td style="padding:.4px 3px">AVERAGE MONTHLY QUOTES</td><td style="padding:.4px 3px">432</td></tr>
      <tr style="background:var(--light)"><td style="padding:.4px 3px">AVERAGE MONTHLY QUOTES</td><td style="padding:.4px 3px">946</td></tr>
      <tr style="background:var(--light)"><td style="padding:.4px 3px">AVERAGE MONTHLY QUOTES</td><td style="padding:.4px 3px">350</td></tr>
      <tr style="background:var(--light)"><td style="padding:.4px 3px">AVERAGE MONTHLY QUOTES</td><td style="padding:.4px 3px">946</td></tr>
      <tr style="background:var(--light)"><td style="padding:.4px 3px">AVERAGE MONTHLY QUOTES</td><td style="padding:.4px 3px">350</td></tr>
    </tbody>
  </table>
  <div class="footer"><span class="footer-name">Presentation Name 2022</span><span class="brand"><i class="brand-dot"></i>GreenGlider</span></div>
</section>

<!-- Benefits -->
<section class="slide" style="left:642px;top:548px">
  <div class="photo" style="left:0;top:0;width:103px;height:131px;background:linear-gradient(160deg,#3a4250 0%,#1f2228 60%,#5a5d63 100%)" role="img" aria-label="Laptop showing a sales chart on a desk"></div>
  <h2 class="title red">BENEFITS</h2>
  <div class="abs" style="left:22px;top:53px;width:46px;height:46px;border-radius:50%;background:var(--black);color:#fff;font-size:3.6px;display:flex;align-items:center;justify-content:center;text-align:center">TOTAL<br>BENEFITS</div>
  <div class="abs" style="left:66px;top:61px;width:30px;height:30px;border-radius:50%;background:var(--red);color:#fff;font-size:3.6px;display:flex;align-items:center;justify-content:center">1296</div>
  <p class="abs caps" style="left:111px;top:16px;width:108px;font-size:2.6px;line-height:1.3">Veniam, quis nostrud exerci tation ullamcorper suscipit lobortis nisl ut aliquip ex ea commodo veniam, quis nostrud exerci tation ullamcorper suscipit lobortis nisl ut aliquip ex ea commodo veniam, quis nostrud exerci tation ullamcorper suscipit lobortis nisl, ut aliquip ex ea com</p>
  <p class="abs caps" style="left:111px;top:55px;font-size:3px;color:#555">Benefits</p>
  <ul class="abs tiny" style="left:113px;top:64px;width:104px;list-style:none">
    <li>&middot; &nbsp;Lorem ipsum dolor sit amet, consectetuer adipiscing elit, sed diam nonummy nibh euismod t</li>
    <li style="margin-top:3px">&middot; &nbsp;tincidunt ut laoreet dolore magna aliquam e</li>
    <li style="margin-top:3px">&middot; &nbsp;rat volutpat. Ut wisi enim ad minim veniam, quis nostrud exerci tation ullamcorper suscipit lobortis nisl ut aliquip ex ea commodo consequat</li>
  </ul>
  <div class="footer"><span class="footer-name">Presentation Name 2022</span><span class="brand"><i class="brand-dot"></i>GreenGlider</span></div>
</section>

<!-- Break -->
<section class="slide" style="left:914px;top:548px">
  <div class="photo" style="left:0;top:0;width:246px;height:131px;background:linear-gradient(180deg,#d9c9a8 0%,#8a9a6a 30%,#4f6b33 55%,#c9b79a 80%,#a89478 100%)" role="img" aria-label="Golf course bunker at sunset"></div>
  <h2 class="title red" style="top:6px">BREAK</h2>
  <div class="footer"><span class="footer-name">Presentation Name 2022</span><span class="brand"><i class="brand-dot"></i>GreenGlider</span></div>
</section>

<!-- Graphic (icons) -->
<section class="slide dark" style="left:66px;top:721px">
  <h2 class="title">GRAPHIC</h2>
  <svg class="abs" style="left:117px;top:17px" width="12" height="12" viewBox="0 0 24 24" fill="none" stroke="#fff" stroke-width="1.6"><path d="M12 2l8 3v6c0 5-3.5 9-8 11-4.5-2-8-6-8-11V5z"/><path d="M8 12l3 3 5-6"/></svg>
  <p class="abs tiny" style="left:80px;top:31px;width:86px;text-align:center">Lorem ipsum dolor sit amet, consectetuer adipiscing elit, sed diam nonummy nibh euismod tincidunt ut laoreet dolore</p>
  <svg class="abs" style="left:68px;top:51px" width="12" height="14" viewBox="0 0 24 28" fill="#fff"><circle cx="12" cy="4" r="3"/><path d="M4 9h16v3h-5v15h-3v-8h-0v8H9V12H4z"/></svg>
  <p class="abs tiny" style="left:30px;top:71px;width:86px;text-align:center">Lorem ipsum dolor sit amet, consectetuer adipiscing elit, sed diam nonummy nibh euismod tincidunt ut laoreet dolore</p>
  <svg class="abs" style="left:166px;top:52px" width="12" height="12" viewBox="0 0 24 24" fill="none" stroke="#fff" stroke-width="1.6"><path d="M8 8l5 13 2-5 5-2z"/><path d="M4 4l2 2M2 9h3M9 2v3"/></svg>
  <p class="abs tiny" style="left:128px;top:71px;width:86px;text-align:center">Lorem ipsum dolor sit amet, consectetuer adipiscing elit, sed diam nonummy nibh euismod tincidunt ut laoreet dolore</p>
  <svg class="abs" style="left:117px;top:96px" width="12" height="12" viewBox="0 0 24 24" fill="none" stroke="#fff" stroke-width="1.6"><rect x="3" y="5" width="18" height="16"/><path d="M3 10h18M8 3v4M16 3v4"/></svg>
  <p class="abs tiny" style="left:80px;top:109px;width:86px;text-align:center">Lorem ipsum dolor sit amet, consectetuer adipiscing elit, sed diam nonummy nibh euismod tincidunt ut laoreet dolore</p>
  <div class="footer"><span class="footer-name">Presentation Name 2022</span><span class="brand"><i class="brand-dot"></i>GreenGlider</span></div>
</section>

<!-- Sector Expertise -->
<section class="slide" style="left:360px;top:721px">
  <div class="abs" style="left:82px;top:62px;width:46px;height:76px;background:var(--light)"></div>
  <h2 class="title red" style="line-height:1.2">SECTOR<br>EXPERTISE</h2>
  <div class="abs" style="left:12px;top:27px;width:200px;display:grid;grid-template-columns:repeat(3,1fr);gap:14px">
    <p class="tiny"><span style="font-size:3.2px">1.</span><br><br>Lorem ipsum dolor sit amet, consectetuer adipiscing elit, sed diam nonummy nibh euismod tincidunt ut laoreet dolore</p>
    <p class="tiny"><span style="font-size:3.2px">2.</span><br><br>Lorem ipsum dolor sit amet, consectetuer adipiscing elit, sed diam nonummy nibh euismod tincidunt ut laoreet dolore</p>
    <p class="tiny"><span style="font-size:3.2px">3.</span><br><br>Lorem ipsum dolor sit amet, consectetuer adipiscing elit, sed diam nonummy nibh euismod tincidunt ut laoreet dolore</p>
  </div>
  <svg class="abs" style="left:0;top:0" width="246" height="138">
    <polygon points="12,62 36,62 59,85 59,138 12,138" fill="#1c1c1e"/>
    <polygon points="84,62 108,62 131,85 131,138 84,138" fill="#e31e24"/>
    <polygon points="156,62 180,62 203,85 203,138 156,138" fill="#1c1c1e"/>
  </svg>
  <p class="abs caps" style="left:21px;top:87px;width:36px;font-size:3px;color:#fff;line-height:1.3">&#9881;<br>Lorem ipsum dolor sit amet, consectetuer</p>
  <p class="abs caps" style="left:93px;top:87px;width:36px;font-size:3px;color:#fff;line-height:1.3">&#9679;<br>Lorem ipsum dolor sit amet, consectetuer</p>
  <p class="abs caps" style="left:165px;top:87px;width:36px;font-size:3px;color:#fff;line-height:1.3">&#9730;<br>Lorem ipsum dolor sit amet, consectetuer</p>
  <div class="footer"><span class="footer-name">Presentation Name 2022</span><span class="brand"><i class="brand-dot"></i>GreenGlider</span></div>
</section>

<!-- Competencies -->
<section class="slide" style="left:642px;top:721px">
  <svg class="abs" style="left:0;top:0" width="246" height="138"><polygon points="0,0 152,0 0,122" fill="#1c1c1e"/></svg>
  <h2 class="title" style="color:#fff">COMPETENCIES</h2>
  <div class="abs" style="left:0;top:0;width:246px;height:138px">
    <div class="abs" style="left:106px;top:24px;display:flex;align-items:center;gap:6px"><span style="width:9px;height:9px;border-radius:50%;background:#555;border:1px solid #fff"></span><span class="caps" style="font-size:2.5px;line-height:1.3">Lorem ipsum dolor sit amet,<br>consectetuer adipiscing elit,</span></div>
    <div class="abs" style="left:82px;top:42px;display:flex;align-items:center;gap:6px"><span style="width:9px;height:9px;border-radius:50%;background:#555;border:1px solid #fff"></span><span class="caps" style="font-size:2.5px;line-height:1.3">Lorem ipsum dolor sit amet,<br>consectetuer adipiscing elit,</span></div>
    <div class="abs" style="left:60px;top:60px;display:flex;align-items:center;gap:6px"><span style="width:9px;height:9px;border-radius:50%;background:#555;border:1px solid #fff"></span><span class="caps" style="font-size:2.5px;line-height:1.3">Lorem ipsum dolor sit amet,<br>consectetuer adipiscing elit,</span></div>
    <div class="abs" style="left:38px;top:80px;display:flex;align-items:center;gap:6px"><span style="width:9px;height:9px;border-radius:50%;background:#555;border:1px solid #fff"></span><span class="caps" style="font-size:2.5px;line-height:1.3">Lorem ipsum dolor sit amet,<br>consectetuer adipiscing elit,</span></div>
    <div class="abs" style="left:16px;top:100px;display:flex;align-items:center;gap:6px"><span style="width:9px;height:9px;border-radius:50%;background:#555;border:1px solid #fff"></span><span class="caps" style="font-size:2.5px;line-height:1.3">Lorem ipsum dolor sit amet,<br>consectetuer adipiscing elit,</span></div>
  </div>
  <div class="footer"><span class="footer-name">Presentation Name 2022</span><span class="brand"><i class="brand-dot"></i>GreenGlider</span></div>
</section>

<!-- Graphic 04 -->
<section class="slide" style="left:914px;top:721px">
  <svg class="abs" style="left:0;top:0" width="246" height="138"><polygon points="0,0 98,0 0,138" fill="#ececec"/><polygon points="98,0 145,0 145,138 0,138" fill="#fff"/><rect x="146" y="0" width="90" height="138" fill="#1c1c1e"/></svg>
  <div class="abs tiny caps" style="left:0;top:0;width:146px;height:138px;text-align:center;font-size:2.4px;color:#555">
    <div class="abs" style="left:63px;top:20px"><span style="display:block;margin:0 auto;width:12px;height:12px;border-radius:50%;background:var(--red)"></span>Management</div>
    <div class="abs" style="left:29px;top:38px"><span style="display:block;margin:0 auto;width:12px;height:12px;border-radius:50%;background:var(--black)"></span>Management</div>
    <div class="abs" style="left:97px;top:38px"><span style="display:block;margin:0 auto;width:12px;height:12px;border-radius:50%;background:var(--black)"></span>Management</div>
    <div class="abs" style="left:29px;top:78px"><span style="display:block;margin:0 auto;width:12px;height:12px;border-radius:50%;background:var(--red)"></span>Management</div>
    <div class="abs" style="left:97px;top:78px"><span style="display:block;margin:0 auto;width:12px;height:12px;border-radius:50%;background:var(--red)"></span>Management</div>
    <div class="abs" style="left:63px;top:96px"><span style="display:block;margin:0 auto;width:12px;height:12px;border-radius:50%;background:var(--black)"></span>Management</div>
  </div>
  <h2 class="title" style="left:150px;color:#fff">GRAPHIC 04</h2>
  <p class="abs tiny" style="left:150px;top:20px;width:78px;color:#fff">Lorem ipsum dolor sit amet, consectetuer adipiscing elit, sed diam nonummy nibh euismod tincidunt ut laoreet dolore magna aliquam erat volutpat. Ut wisi enim ad minim veniam, quis nostrud exerci tation ullamcorper suscipit lobortis nisl ut aliquip ex ea commodo consequat. Duis autem vel eum iriure dolor in hendrerit in vulputate velit esse molestie consequat, vel illum dolore eu feugiat nulla facilisis at vero eros et accumsan et iusto odio dignissim qui blandit praesent luptatum zzril delenit augue duis dolore te feugait nulla facilisi. Lorem ipsum dolor sit amet, cons ectetuer adipiscing elit, sed diam nonummy nibh euismod tincidunt ut laoreet dolore magna aliquam erat volutpat.</p>
  <div class="footer"><span class="footer-name">Presentation Name 2022</span><span class="brand"><i class="brand-dot"></i>GreenGlider</span></div>
</section>

<!-- Methods of Differentiation -->
<section class="slide" style="left:66px;top:894px">
  <div class="photo" style="left:0;top:0;width:246px;height:138px;background:radial-gradient(circle at 50% 55%,#e2542e 0%,#c9441f 55%,#a8351a 100%)" role="img" aria-label="Putter and ball on turf, tinted red"></div>
  <div class="abs" style="left:0;top:0;width:100px;height:24px;background:var(--black);border-radius:0 0 6px 0"></div>
  <h2 class="title bold" style="color:#fff;top:6px;line-height:1.2">METHODS OF<br>DIFFERENTIATION</h2>
  <div class="abs tiny" style="left:20px;top:34px;width:50px;text-align:center;color:#f6c1b0">&#10004;<br>Network of Providers<br><br>Lorem ipsum dolor sit amet, consectetuer adipiscing elit, sed diam nonummy nibh euismod</div>
  <div class="abs tiny" style="left:98px;top:55px;width:52px;text-align:center;color:#f6c1b0">&#10004;<br>Network of Providers<br><br>Lorem ipsum dolor sit amet, consectetuer adipiscing elit, sed diam nonummy nibh euismod</div>
  <div class="abs tiny" style="left:176px;top:34px;width:54px;text-align:center;color:#f6c1b0">&#10004;<br>Network of Providers<br><br>Lorem ipsum dolor sit amet, consectetuer adipiscing elit, sed diam nonummy nibh euismod</div>
  <div class="footer"><span class="footer-name">Presentation Name 2022</span><span class="brand"><i class="brand-dot"></i>GreenGlider</span></div>
</section>

<!-- About Us (circle) -->
<section class="slide" style="left:360px;top:894px">
  <h2 class="title red">ABOUT US</h2>
  <div class="photo photo-golf photo-round" style="left:15px;top:26px;width:88px;height:88px" role="img" aria-label="Golfer on the fairway"></div>
  <p class="abs tiny" style="left:120px;top:30px;width:50px">Lorem ipsum dolor sit amet, consectetuer adipiscing elit, sed diam nonummy nibh euismod tincidunt ut laoreet dolore magna aliquam erat volutpat. Ut wisi enim ad minim veniam, quis nostrud exerci tation ullamcorper suscipit lobortis nisl ut aliquip ex ea commodo consequat. Duis autem vel eum iriure dolor in hendrerit in vulputate velit esse molestie consequat, vel illum dolore eu feugiat nulla facilisis at vero eros et accumsan et iusto odio dignissim qui blandit praesent luptatum zzril delenit augue duis dolore te feugait nulla facilisi.<br><br>Lorem ipsum dolor sit amet,</p>
  <p class="abs tiny" style="left:182px;top:30px;width:50px">Lorem ipsum dolor sit amet, consectetuer adipiscing elit, sed diam nonummy nibh euismod tincidunt ut laoreet dolore magna aliquam erat volutpat. Ut wisi enim ad minim veniam, quis nostrud exerci tation ullamcorper suscipit lobortis nisl ut aliquip ex ea commodo consequat. Duis autem vel eum iriure dolor in hendrerit in vulputate velit esse molestie consequat, vel illum dolore eu feugiat nulla facilisis at vero eros et accumsan et iusto odio dignissim qui blandit praesent luptatum zzril delenit augue duis dolore te feugait nulla facilisi.<br><br>Lorem ipsum dolor sit amet,</p>
  <div class="footer"><span class="footer-name">Presentation Name 2022</span><span class="brand"><i class="brand-dot"></i>GreenGlider</span></div>
</section>

<!-- Outline -->
<section class="slide dark" style="left:642px;top:894px">
  <h2 class="title">OUTLINE</h2>
  <div class="abs" style="left:9px;top:34px;width:216px;display:grid;grid-template-columns:repeat(4,1fr);gap:9px 3px">
    <div style="background:var(--red);height:24px;display:flex;align-items:center;padding-left:4px;font-size:3.4px"><b style="font-size:9px;font-weight:500">1.</b>&nbsp;SUMMARY</div>
    <div style="background:var(--red);height:24px;display:flex;align-items:center;padding-left:4px;font-size:3.4px"><b style="font-size:9px;font-weight:500">2.</b>&nbsp;VISION</div>
    <div style="background:var(--red);height:24px;display:flex;align-items:center;padding-left:4px;font-size:3.4px"><b style="font-size:9px;font-weight:500">3.</b>&nbsp;SUMMARY</div>
    <div style="background:var(--red);height:24px;display:flex;align-items:center;padding-left:4px;font-size:3.4px"><b style="font-size:9px;font-weight:500">4.</b>&nbsp;VISION</div>
    <div style="background:var(--red);height:24px;display:flex;align-items:center;padding-left:4px;font-size:3.4px"><b style="font-size:9px;font-weight:500">5.</b>&nbsp;SUMMARY</div>
    <div style="background:var(--red);height:24px;display:flex;align-items:center;padding-left:4px;font-size:3.4px"><b style="font-size:9px;font-weight:500">6.</b>&nbsp;VISION</div>
    <div style="background:var(--red);height:24px;display:flex;align-items:center;padding-left:4px;font-size:3.4px"><b style="font-size:9px;font-weight:500">7.</b>&nbsp;SUMMARY</div>
    <div style="background:var(--red);height:24px;display:flex;align-items:center;padding-left:4px;font-size:3.4px"><b style="font-size:9px;font-weight:500">8.</b>&nbsp;VISION</div>
  </div>
  <p class="abs tiny" style="left:12px;top:105px;width:160px">Lorem ipsum dolor sit amet, consectetuer adipiscing elit, sed diam nonummy nibh euismod tincidunt ut laoreet dolore magna aliquam erat volutpat. Ut wisi enim ad minim veniam, quis nostrud exerci tation ullamcorper suscipit lobortis nisl ut aliquip ex ea commodo consequat.</p>
  <div class="footer"><span class="footer-name">Presentation Name 2022</span><span class="brand"><i class="brand-dot"></i>GreenGlider</span></div>
</section>

<!-- Thank You -->
<section class="slide dark" style="left:914px;top:894px">
  <h2 class="title" style="font-size:8.5px;font-weight:400">THANK YOU</h2>
  <p class="abs caps" style="left:12px;top:31px;width:90px;font-size:5.3px;line-height:1.25">Lorem ipsum dolor sit amet, consectetuer adipiscing elit, sed di</p>
  <div class="photo photo-golf photo-round" style="left:113px;top:6px;width:112px;height:112px" role="img" aria-label="Golfer swinging on a sunny course"></div>
  <div class="footer"><span class="footer-name">Presentation Name 2022</span><span class="brand"><i class="brand-dot"></i>GreenGlider</span></div>
</section>

</body>
</html>
```